Corporate services company needs a brochure

We are starting a company offering setup services to companies new to that location.
This includes services such as recruitment, company formation, advertising, marketing, pr, handling legal issues, logistics, transportation, procurement,immigration services, corporate gifts, accomodation,entertainment, training, administrative services etc.
Basically taking the setup issues off the hands of the company allowing them focus on their core business.

We are looking to design a professional brochure which would give the potential customers the confidence to entrust us with their needs.

We will be including some copy that can be used but i would very much like for you to bring what i have written to life - adding, deducting and amending where required.

We are looking at a A4 4/6 paged brochure but open to suggestions.

                                       

If you have any images that are suitable, please let us know. We will also be searching for some to add.

The first prize has been increased.

Thanks

Reason: We have just guaranteed the payment and we are hoping that this will encourage good designers to participate.

Reason: Some designers have requested more time to complete their final design.

Hi, I h extended the deadline to give designers more time to work on designs.

we are also looking at making the brochure a height of 8.5 and a width of 11. Please let me know your thoughts on this as any advice will help. The whole objective is to make it look as up to date and creative as possible. There is also another design size of 7.5 by 8.5

Thanks

                                        Hi

The copy has been revised and uploaded.

Hopefully it will give a clearer explanation of what we are trying to do.

Please let me know if you have any further questions.

Thanks

Mabel

Reason: adding finishing touches to designs

Reason: We are amending the copy for the brochure

Reason: The new copy for the brochure is ready. I am sorry it has taken so long to get it out. I am sure we will not be making any amendments to it post today. Thanks for your patience The extension is not to attact new designs it is for existing designs's copy to be modified to include information from the updated copy.

medium to large companies in banking, telecom, retail etc. It will be viewed by middle and top management.

Legal

• The brochure must clearly highlight all our services without just listing as this would risk it appearing as if we have just included everything we could think of!,
Please do not do the sitting round the conference table brochure or the typical blue and white brochure.
I desperately need it to be different, unique and serious enough to show that we are capable of handling/managing all what we have included.
Our clients include the many companies starting up an office in Africa.
We are anxious to have the potential clients understand that we will help them setup under any climax/
• modern colours but not too bright. there must still be a clear serious edge to it.
• conference room table and people sitting around it.
the typical blue and white brochures often used for these type of services.

```html
<!DOCTYPE html>
<html lang="en">
<head>
<meta charset="utf-8">
<title>Orvane Brochure Covers</title>
<link rel="stylesheet" href="https://fonts.googleapis.com/css2?family=Jost:wght@400;500&display=swap">
<style>
  :root {
    --backdrop: #1c1d1f;
    --cover-dark: #30343a;
    --cover-light: #4a5058;
    --ink-light: #f2f3f4;
    --ink-muted: #a9adb3;
    --rule: #e9eaec;
    --dot-red: rgba(236, 96, 104, 0.78);
    --dot-yellow: rgba(246, 222, 40, 0.85);
    --dot-purple: rgba(96, 52, 140, 0.9);
    --photo-a: #8a8e94;
    --photo-b: #c9b6a2;
    --photo-c: #4a4e55;
  }
  * { box-sizing: border-box; margin: 0; padding: 0; }
  html, body {
    width: 1200px; height: 793px; overflow: hidden;
    background: var(--backdrop);
    font-family: "Jost", sans-serif;
  }
  .cover {
    position: absolute; top: 145px;
    width: 504px; height: 504px;
    background: radial-gradient(ellipse at 50% 40%, var(--cover-light) 0%, var(--cover-dark) 70%);
    box-shadow: 0 6px 18px rgba(0,0,0,0.55);
    overflow: hidden;
  }
  .cover--back { left: 70px; }
  .cover--front { left: 626px; }

  .brand-name {
    color: var(--ink-light);
    font-weight: 500;
    letter-spacing: 2px;
    text-transform: uppercase;
  }
  .cover--back .brand-name {
    position: absolute; top: 384px; left: 0; width: 100%;
    text-align: center; font-size: 26px;
  }
  .contact {
    position: absolute; top: 424px; left: 0; width: 100%;
    text-align: center; color: var(--ink-muted);
    font-size: 10.5px; line-height: 13px;
  }

  .cover--front .brand-name {
    position: absolute; top: 58px; right: 30px;
    font-size: 26px;
  }
  .feature-band {
    position: absolute; left: 4px; right: 0; top: 208px; height: 204px;
    border-top: 3px solid var(--rule);
    border-bottom: 3px solid var(--rule);
  }
  .feature-photo {
    width: 100%; height: 100%;
    background: linear-gradient(100deg, var(--photo-a) 0%, var(--photo-b) 55%, var(--photo-c) 100%);
  }
  .dot { position: absolute; border-radius: 50%; }
  .dot--red { left: 12px; top: 66px; width: 136px; height: 136px; background: var(--dot-red); }
  .dot--yellow { left: 106px; top: 110px; width: 80px; height: 80px; background: var(--dot-yellow); }
  .dot--purple { left: 99px; top: 361px; width: 44px; height: 44px; background: var(--dot-purple); }
  .intro-copy {
    position: absolute; left: 26px; top: 82px; width: 110px;
    color: var(--ink-light); font-size: 7px; line-height: 9.4px;
    text-align: justify;
  }
  .web {
    position: absolute; bottom: 26px; left: 0; width: 100%;
    text-align: center; padding-left: 70px;
    color: var(--ink-light); font-size: 9.5px;
  }
</style>
</head>
<body>
  <section class="cover cover--back">
    <div class="brand-name">Orvane</div>
    <address class="contact">
      Palmgrove Court,<br>
      Marina Point, Lagos Nigeria<br>
      services@orvanegroup.com<br>
      www.orvanegroup.com
    </address>
  </section>

  <section class="cover cover--front">
    <div class="brand-name">Orvane</div>
    <div class="feature-band">
      <div class="feature-photo" role="img" aria-label="Photo of business people applauding in an office"></div>
    </div>
    <div class="dot dot--red" style="top:274px"></div>
    <div class="dot dot--yellow" style="top:318px"></div>
    <div class="dot dot--purple"></div>
    <p class="intro-copy" style="top:290px">Founded in 2007, Orvane offers services to startup companies that help them build their idea into a thriving business. We offer advice and expertise and provide services essential to running the day-to-day operation or both the consultation and the heavy lifting needed to grow your company.</p>
    <div class="web">www.orvanegroup.com</div>
  </section>
</body>
</html>
```